Paper Lantern Theory - Podcast Cover

Paper Lantern Theory is a weekly podcast that dispels some of the myths about conventional economic thinking and provides a new way of thinking about issues that are faced by the global economy. It's insightful, thought-provoking and, most importantly, fun. We are refreshing the look and sound of the podcast. I have attached a copy of the old amateur design (which I did!)

Target Market(s)

Male oriented, smart folk with an interest in politics and economics

Font styles to use
Sans Serif

Requirements
Must have
• Clearly visible title, even when reduced in size. Must be 3000 pixels by 3000 pixels.
Nice to have
• This podcast challenges the status quo. It should reflect that. Photos and names of the hosts. Actually, because th ephotos are so different, we'd be open to the idea of a caricature if you can do that within the price.

```html
<!DOCTYPE html>
<html lang="en">
<head>
<meta charset="utf-8">
<title>Paper Lantern Theory – Podcast Cover</title>
<link rel="stylesheet" href="https://fonts.googleapis.com/css2?family=Oswald:wght@500;600&family=Roboto+Condensed:wght@700&display=swap">
<style>
  :root {
    --page-bg: #e9e7e4;
    --cover-bg: #ffffff;
    --title-red: #c4161c;
    --ink: #1d1d1b;
    --money-light: #e4e6df;
    --money-dark: #8f9a86;
    --host-left-light: #e8e6e2;
    --host-left-dark: #9a9389;
    --host-right-light: #7fb6d0;
    --host-right-dark: #2f7fa6;
  }
  html, body {
    margin: 0;
    width: 1200px;
    height: 807px;
    overflow: hidden;
    background: var(--page-bg);
  }
  .podcast-cover {
    position: absolute;
    left: 230px;
    top: 33px;
    width: 740px;
    height: 740px;
    background: var(--cover-bg);
    box-shadow: 0 6px 24px rgba(0,0,0,0.18);
  }
  .podcast-cover svg { display: block; }
  .title-the, .title-main, .title-sub {
    font-family: "Oswald", "Arial Narrow", sans-serif;
  }
  .title-the { font-weight: 600; font-size: 42px; fill: var(--ink); }
  .title-main { font-weight: 500; font-size: 112px; fill: var(--title-red); }
  .title-sub { font-weight: 500; font-size: 112px; fill: var(--ink); }
  .title-podcast {
    font-family: "Roboto Condensed", "Arial Narrow", sans-serif;
    font-weight: 700; font-size: 25px; fill: var(--ink); letter-spacing: 2px;
  }
  .host-name {
    font-family: "Roboto Condensed", "Arial Narrow", sans-serif;
    font-weight: 700; font-size: 19px; fill: var(--ink);
  }
  .host-divider { stroke: var(--ink); stroke-width: 2.5; }
</style>
</head>
<body>
  <div class="podcast-cover">
    <svg width="740" height="740" viewBox="0 0 740 740" xmlns="http://www.w3.org/2000/svg">
      <defs>
        <linearGradient id="money-tone" x1="0" y1="0" x2="1" y2="1">
          <stop offset="0" stop-color="var(--money-light)"/>
          <stop offset="1" stop-color="var(--money-dark)"/>
        </linearGradient>
        <linearGradient id="host-left-tone" x1="0" y1="0" x2="0" y2="1">
          <stop offset="0" stop-color="var(--host-left-light)"/>
          <stop offset="1" stop-color="var(--host-left-dark)"/>
        </linearGradient>
        <linearGradient id="host-right-tone" x1="0" y1="0" x2="0" y2="1">
          <stop offset="0" stop-color="var(--host-right-light)"/>
          <stop offset="1" stop-color="var(--host-right-dark)"/>
        </linearGradient>
      </defs>

      <g class="cover-title">
        <text class="title-the" x="370" y="92" text-anchor="middle">THE</text>
        <text class="title-main" x="370" y="222" text-anchor="middle" textLength="640" lengthAdjust="spacingAndGlyphs">PAPER LANTERN</text>
        <text class="title-sub" x="370" y="338" text-anchor="middle" textLength="420" lengthAdjust="spacing">THEORY</text>
        <text class="title-podcast" x="370" y="377" text-anchor="middle">PODCAST</text>
      </g>

      <rect class="money-visual" x="205" y="408" width="300" height="205" rx="6"
            fill="url(#money-tone)" role="img" aria-label="Banknotes curling down into a drain hole"/>

      <rect class="host-photo host-photo--left" x="0" y="478" width="185" height="262"
            fill="url(#host-left-tone)" role="img" aria-label="Photo of host Prof. Alan Marsh, arms crossed, in a light t-shirt"/>
      <rect class="host-photo host-photo--right" x="510" y="490" width="230" height="250"
            fill="url(#host-right-tone)" role="img" aria-label="Photo of host Tom Pellow smiling, in a blue polo shirt"/>

      <g class="host-names">
        <text class="host-name" x="282" y="711" text-anchor="middle">PROF. ALAN MARSH</text>
        <line class="host-divider" x1="378" y1="682" x2="378" y2="716"/>
        <text class="host-name" x="452" y="711" text-anchor="middle">TOM PELLOW</text>
      </g>
    </svg>
  </div>
</body>
</html>
```